I need a great, modern, professional website for my paint contracting company, Brookhollow Paint Contractors, LLC. I have many good pix that can be used from jobs completed that would be attractive. We do commercial, residential and industrial jobs. I’m fully insured and licensed, including holding a General Contractor’s License as a Subcontractor. I know nothing about coding websites. I’ll have my assistant get on tomorrow and learn how to drop files. I’m not sure what files to send. This will be difficult at best, it being able to talk this through. Oh well. What’s next?

Target Market(s)

General Contractors

Industry/Entity Type

Paint Contracting

Coding

Coded - Design and coding required

Font styles to use
Sans Serif

Colors
00AB8E
00BBA5
67D7C9
C6EFE9
E9F9F6

Requirements
Must have
• Pix of completed jobs, bio, maybe testimonials from happy customers? ….
Nice to have
• I’d like it to have a modern appeal, but still have some warmth.
Should not have
• ??

```html
<!DOCTYPE html>
<html lang="en">
<head>
<meta charset="utf-8">
<title>Brookhollow Paint Contractors, LLC</title>
<link href="https://fonts.googleapis.com/css2?family=Crimson+Pro:wght@400;500;600;700&family=Poppins:wght@400;500;600&display=swap" rel="stylesheet">
<style>
:root{
  --green-dark:#0d5e4b;
  --green:#0f6b55;
  --teal:#12a38a;
  --teal-light:#00bba5;
  --mint:#c6efe9;
  --mint-band:#e4eeec;
  --grey-bg:#f5f5f5;
  --text:#222;
  --footer:#232323;
  --footer-bar:#1a1a1a;
  --white:#fff;
}
*{margin:0;padding:0;box-sizing:border-box}
html,body{width:1200px;height:4717px;overflow:hidden}
body{font-family:'Poppins',sans-serif;color:var(--text);background:var(--white);position:relative}
.abs{position:absolute}
.btn{position:absolute;display:flex;align-items:center;justify-content:center;font-family:'Crimson Pro',serif;font-size:13px;letter-spacing:.5px;color:var(--white);background:var(--green);border:2px solid var(--green);box-shadow:inset 0 0 0 2px var(--white);text-transform:uppercase;height:34px;white-space:nowrap}
.btn.teal{background:var(--teal);border-color:var(--teal)}
.section-title{position:absolute;left:0;width:1200px;text-align:center;font-family:'Crimson Pro',serif;font-weight:600;font-size:36px;color:var(--green-dark);letter-spacing:1px;text-transform:uppercase}
.section-title span{border-bottom:2px solid var(--green-dark);padding-bottom:2px}
.photo{position:absolute}

/* header */
.site-header{position:absolute;top:0;left:0;width:1200px;height:94px;background:var(--white)}
.brand{left:88px;top:20px;font-family:'Crimson Pro',serif;font-weight:600;font-size:44px;color:var(--green-dark);font-variant:small-caps;letter-spacing:1px;white-space:nowrap}
.nav{left:536px;top:60px;display:flex;gap:22px;font-family:'Crimson Pro',serif;font-size:14px;color:#333;white-space:nowrap}
.nav .active{color:var(--teal);border-bottom:2px solid var(--teal);padding-bottom:4px}
.header-phone{left:778px;top:16px;display:flex;align-items:center;gap:8px;font-family:'Crimson Pro',serif;font-size:16px}
.icon-circle{width:26px;height:26px;border-radius:50%;background:var(--green-dark);display:flex;align-items:center;justify-content:center}

/* hero */
.hero{top:94px;left:0;width:1200px;height:504px;background:
  radial-gradient(ellipse 520px 180px at 560px 40px,rgba(240,232,214,.75),transparent 70%),
  radial-gradient(ellipse 260px 120px at 1040px 260px,rgba(236,226,204,.55),transparent 70%),
  linear-gradient(180deg,#d8cfbf 0%,#a58c74 18%,#7b6351 45%,#6a5242 75%,#4e3b2f 100%)}
.hero::after{content:"";position:absolute;inset:0;background:linear-gradient(180deg,rgba(0,0,0,0) 30%,rgba(0,0,0,.18) 100%)}
.hero-title{position:absolute;z-index:1;top:190px;left:0;width:1200px;text-align:center;font-family:'Crimson Pro',serif;font-weight:600;font-size:37px;line-height:48px;color:var(--white);text-transform:uppercase;letter-spacing:1px}
.dots{position:absolute;display:flex;gap:14px;z-index:1}
.dot{width:14px;height:14px;border-radius:50%;border:2px solid var(--white)}
.dot.on{background:var(--teal);border-color:var(--teal)}

/* welcome */
.welcome-title{left:88px;top:718px;font-family:'Crimson Pro',serif;font-weight:700;font-size:36px;color:var(--green-dark)}
.welcome-title span{border-bottom:2px solid var(--green-dark)}
.welcome-lead{left:90px;top:782px;width:440px;font-size:15px;font-weight:500;line-height:24px}
.welcome-text{left:90px;top:855px;width:560px;font-size:11.5px;line-height:19px;color:#333}
.signature{left:88px;top:966px;font-family:'Crimson Pro',serif;font-size:16px;color:var(--green-dark)}
.signature small{display:block;font-size:11px;color:#333;line-height:10px}
.dot-pattern{background-image:radial-gradient(#b8d7cf 1.3px,transparent 1.4px);background-size:7px 7px}

/* services */
.service-row{position:absolute;left:0;width:1200px;height:379px;background:var(--grey-bg)}
.service-copy{position:absolute;width:440px}
.service-copy h3{font-family:'Crimson Pro',serif;font-weight:600;font-size:22px;color:var(--green-dark);letter-spacing:.5px;margin-bottom:10px}
.service-copy p{font-size:12px;line-height:21px;color:#333}

/* industry */
.industry-card{position:absolute;width:325px}
.industry-card .img{height:160px}
.industry-card h4{font-family:'Crimson Pro',serif;font-weight:600;font-size:17px;color:var(--green-dark);margin-top:20px}
.industry-card p{font-size:11.5px;line-height:19px;color:#333;margin-top:2px}
.arrow{position:absolute;width:26px;height:26px;border-radius:50%;display:flex;align-items:center;justify-content:center}
.arrow.grey{background:#cfcfcf}
.arrow.green{background:var(--teal)}

/* features */
.features{top:2918px;left:0;width:1200px;height:239px;background:var(--mint-band)}
.feature{position:absolute;top:55px;width:240px;text-align:center}
.feature .tile{width:66px;height:66px;margin:0 auto;background:var(--white);box-shadow:0 2px 6px rgba(0,0,0,.08);display:flex;align-items:center;justify-content:center}
.feature p{font-family:'Crimson Pro',serif;font-size:17px;margin-top:18px;color:#222}
.small-dot{width:10px;height:10px;border-radius:50%;border:1.5px solid #9ccfc4}
.small-dot.on{border-color:var(--teal);background:radial-gradient(var(--teal) 2px,transparent 2.5px)}

/* partners */
.partner{position:absolute;top:3303px;width:208px;height:83px;background:var(--white);border:1px solid #e2e2e2;box-shadow:0 2px 8px rgba(0,0,0,.06);display:flex;align-items:center;justify-content:center}
.partner .mark{width:150px;height:40px;display:flex;align-items:center;gap:12px}
.partner .mark i{width:40px;height:40px;border-radius:50%;display:block}
.partner .mark b{flex:1;height:16px;background:#555;border-radius:2px;opacity:.75}

/* testimonial */
.testimonial{top:3534px;left:0;width:1200px;height:374px;background:var(--green-dark)}
.quote{position:absolute;left:208px;top:120px;width:520px;font-size:16px;line-height:29px;color:var(--white)}
.rating{position:absolute;left:208px;top:80px;display:flex;gap:4px;align-items:center;color:#5fc9b4;font-size:12px}
.rule{position:absolute;left:208px;top:228px;width:565px;height:1px;background:rgba(255,255,255,.2)}
.author{position:absolute;left:290px;top:250px;font-size:14px;color:var(--white);line-height:22px}
.author .name{color:#3fbf9e}
.vdots{position:absolute;left:139px;top:152px;display:flex;flex-direction:column;gap:12px}
.vdots .small-dot{border-color:var(--white);width:12px;height:12px}
.vdots .small-dot.on{border-color:#3fbf9e;background:radial-gradient(#3fbf9e 2px,transparent 2.5px)}

/* form */
.field{position:absolute;height:36px;border:1px solid #ddd;display:flex;align-items:center;gap:10px;padding-left:16px;font-size:11.5px;color:#aaa}

/* footer */
.site-footer{top:4388px;left:0;width:1200px;height:295px;background:var(--footer)}
.footer-bar{top:4683px;left:0;width:1200px;height:34px;background:var(--footer-bar)}
.footer-brand{position:absolute;left:88px;top:88px;font-family:'Crimson Pro',serif;font-weight:600;font-size:27px;color:var(--teal-light);letter-spacing:1px;text-transform:uppercase;white-space:nowrap}
.col-title{position:absolute;font-family:'Crimson Pro',serif;font-size:18px;color:var(--teal)}
.contact-line{position:absolute;left:408px;display:flex;gap:14px;font-size:12px;color:#ddd;line-height:19px}
.quick-links{position:absolute;left:690px;top:70px;font-size:12px;color:#ddd;line-height:25px;list-style:none}
.quick-links .current{color:var(--teal);text-decoration:underline}
.social{position:absolute;top:8px;right:88px;display:flex;gap:12px}
.social i{width:18px;height:18px;border-radius:50%;background:#ddd;display:block}
</style>
</head>
<body>

<header class="site-header">
  <div class="abs brand">Brookhollow Paint</div>
  <nav class="abs nav">
    <span class="active">HOME</span><span>ABOUT US</span><span>SERVICES</span><span>INDUSTRIES</span><span>TESTIMONIALS</span><span>CONTACT US</span>
  </nav>
  <div class="abs header-phone">
    <span class="icon-circle"><svg width="13" height="13" viewBox="0 0 24 24"><path fill="#fff" d="M6.6 10.8a15 15 0 006.6 6.6l2.2-2.2c.3-.3.7-.4 1-.2 1.1.4 2.3.6 3.6.6.6 0 1 .4 1 1V20c0 .6-.4 1-1 1A17 17 0 013 4c0-.6.4-1 1-1h3.5c.6 0 1 .4 1 1 0 1.3.2 2.5.6 3.6.1.3 0 .7-.2 1z"/></svg></span>
    +1 555-014-2290
  </div>
  <div class="btn teal" style="left:952px;top:12px;width:108px;height:34px;font-size:12px">Get an Estimate</div>
</header>

<section class="abs hero" role="img" aria-label="Photo of a finished hotel ballroom interior with brick walls and chandeliers">
  <h1 class="hero-title">We specialize in residential<br>and commercial painting and<br>construction.</h1>
  <div class="dots" style="left:562px;top:470px"><span class="dot"></span><span class="dot on"></span><span class="dot"></span></div>
</section>

<div class="abs dot-pattern" style="left:936px;top:676px;width:176px;height:24px"></div>
<div class="abs dot-pattern" style="left:724px;top:740px;width:18px;height:312px"></div>
<div class="abs dot-pattern" style="left:724px;top:1033px;width:176px;height:20px"></div>
<h2 class="abs welcome-title"><span>WEL</span>COME!</h2>
<p class="abs welcome-lead">Lorem Ipsum is simply dummy text of the printing and typesetting industry.</p>
<p class="abs welcome-text">Lorem Ipsum has been the industry's standard dummy text ever since the 1500s, when an unknown printer took a galley of type and scrambled it to make a type specimen book. It has survived not only five centuries, but also the leap into electronic typesetting, remaining essentially unchanged.</p>
<div class="abs signature">Dana Morrow<small>CEO</small></div>
<div class="btn" style="left:198px;top:968px;width:106px">About Us</div>
<div class="photo" style="left:742px;top:696px;width:370px;height:337px;background:radial-gradient(ellipse 150px 170px at 50% 38%,#c9a48a 0%,#8a6a55 45%,transparent 72%),linear-gradient(180deg,#eeeeee 0%,#e4e4e4 60%,#2a2a2a 82%,#151515 100%)" role="img" aria-label="Portrait photo of the company owner"></div>

<h2 class="section-title" style="top:1122px"><span>SER</span>VICES</h2>
<p class="abs" style="left:0;top:1174px;width:1200px;text-align:center;font-size:13px">Our team can help you with any project from start to finish.</p>

<div class="service-row" style="top:1228px">
  <div class="photo" style="left:0;top:0;width:600px;height:379px;background:radial-gradient(ellipse 210px 170px at 50% 52%,#f1f0ea 0%,#e0ded6 55%,transparent 75%),linear-gradient(180deg,#c5c8c6 0%,#aeb2ae 30%,#8c9a86 55%,#55703f 78%,#3f5a2e 100%)" role="img" aria-label="Photo of a painted white two-storey house with a porch"></div>
  <div class="service-copy" style="left:672px;top:100px">
    <h3>RESIDENTIAL</h3>
    <p>Lorem Ipsum is simply dummy text of the printing and typesetting industry. Lorem Ipsum has been the industry's standard dummy text ever since the 1500s, when an unknown printer took a galley of type and scrambled it to make a type specimen book.</p>
  </div>
  <div class="btn teal" style="left:672px;top:240px;width:146px">Find Out More</div>
</div>

<div class="service-row" style="top:1607px">
  <div class="service-copy" style="left:88px;top:100px">
    <h3>COMMERCIAL</h3>
    <p>Lorem Ipsum is simply dummy text of the printing and typesetting industry. Lorem Ipsum has been the industry's standard dummy text ever since the 1500s, when an unknown printer took a galley of type and scrambled it to make a type specimen book.</p>
  </div>
  <div class="btn" style="left:88px;top:240px;width:146px">Find Out More</div>
  <div class="photo" style="left:600px;top:0;width:600px;height:379px;background:radial-gradient(ellipse 240px 120px at 62% 52%,#c9ccc6 0%,#a8aca6 50%,transparent 75%),linear-gradient(180deg,#8d97a3 0%,#a9b0b6 35%,#6f7a6c 62%,#55574f 80%,#3f403b 100%)" role="img" aria-label="Photo of a painted church building with a steeple"></div>
</div>

<div class="service-row" style="top:1986px">
  <div class="photo" style="left:0;top:0;width:600px;height:377px;background:radial-gradient(ellipse 160px 140px at 90% 45%,#e4e4e6 0%,#cfd0d3 50%,transparent 75%),linear-gradient(180deg,#9fb1cc 0%,#b3bfd0 30%,#8e9299 55%,#9a7c62 78%,#7a5a44 100%)" role="img" aria-label="Photo of a steel frame industrial building under construction"></div>
  <div class="service-copy" style="left:672px;top:100px">
    <h3>INDUSTRIAL</h3>
    <p>Lorem Ipsum is simply dummy text of the printing and typesetting industry. Lorem Ipsum has been the industry's standard dummy text ever since the 1500s, when an unknown printer took a galley of type and scrambled it to make a type specimen book.</p>
  </div>
  <div class="btn teal" style="left:672px;top:240px;width:146px">Find Out More</div>
</div>

<h2 class="section-title" style="top:2434px"><span>SER</span>VICES BY INDUSTRY</h2>
<div class="arrow grey" style="left:50px;top:2632px"><svg width="12" height="12" viewBox="0 0 12 12"><path d="M8 2L4 6l4 4" stroke="#fff" stroke-width="2" fill="none"/></svg></div>
<div class="arrow green" style="left:1124px;top:2632px"><svg width="12" height="12" viewBox="0 0 12 12"><path d="M4 2l4 4-4 4" stroke="#fff" stroke-width="2" fill="none"/></svg></div>

<div class="industry-card" style="left:88px;top:2515px">
  <div class="img" style="background:radial-gradient(ellipse 160px 70px at 55% 55%,#7f8584 0%,#6c7170 50%,transparent 78%),linear-gradient(180deg,#3e68a6 0%,#5a7fb0 30%,#6f7471 58%,#4d6a55 85%,#3f5a45 100%)" role="img" aria-label="Photo of painted townhomes"></div>
  <h4>HOMES</h4>
  <p>Lorem Ipsum is simply dummy text of the printing and typesetting industry. Lorem Ipsum has been the industry's standard dummy.</p>
</div>
<div class="industry-card" style="left:437px;top:2515px">
  <div class="img" style="background:radial-gradient(ellipse 70px 110px at 45% 45%,#eef0f2 0%,#d7dade 55%,transparent 80%),linear-gradient(180deg,#6f9fd6 0%,#a9c5e6 45%,#cfd6dc 70%,#5b8a45 90%,#3f6b30 100%)" role="img" aria-label="Photo of a high rise residential tower"></div>
  <h4>HIGH RISE</h4>
  <p>Lorem Ipsum is simply dummy text of the printing and typesetting industry. Lorem Ipsum has been the industry's standard dummy.</p>
</div>
<div class="industry-card" style="left:787px;top:2515px">
  <div class="img" style="background:radial-gradient(ellipse 200px 50px at 50% 40%,#aab2b6 0%,#7f898e 50%,transparent 80%),linear-gradient(180deg,#2f3840 0%,#55606a 35%,#8a9598 62%,#7e9478 82%,#98a39a 100%)" role="img" aria-label="Photo of a manufacturing warehouse interior with lifts"></div>
  <h4>MANUFACTURING</h4>
  <p>Lorem Ipsum is simply dummy text of the printing and typesetting industry. Lorem Ipsum has been the industry's standard dummy.</p>
</div>

<div class="btn" style="left:428px;top:2820px;width:106px">View All</div>
<div class="btn" style="left:542px;top:2820px;width:92px">Call Us</div>
<div class="btn teal" style="left:642px;top:2820px;width:130px">Get a Quote</div>

<section class="abs features">
  <div class="feature" style="left:90px">
    <div class="tile"><svg width="40" height="40" viewBox="0 0 40 40"><circle cx="20" cy="20" r="13" stroke="#333" stroke-width="2" fill="none"/><path d="M20 12v8h6" stroke="#333" stroke-width="2" fill="none"/><circle cx="28" cy="28" r="6" fill="#0d5e4b"/><path d="M25 28l2 2 4-4" stroke="#fff" stroke-width="1.5" fill="none"/></svg></div>
    <p>On-time delivery</p>
  </div>
  <div class="feature" style="left:323px">
    <div class="tile"><svg width="40" height="40" viewBox="0 0 40 40"><rect x="7" y="13" width="26" height="15" rx="2" stroke="#333" stroke-width="2" fill="none"/><circle cx="20" cy="20.5" r="4" stroke="#0d5e4b" stroke-width="2" fill="none"/><path d="M10 31h20" stroke="#333" stroke-width="2"/></svg></div>
    <p>Competitive pricing</p>
  </div>
  <div class="feature" style="left:564px">
    <div class="tile"><svg width="40" height="40" viewBox="0 0 40 40"><rect x="9" y="7" width="22" height="26" rx="1" stroke="#333" stroke-width="2" fill="none"/><path d="M13 14h14M13 19h14M13 24h8" stroke="#333" stroke-width="2"/><circle cx="27" cy="28" r="5" fill="#0d5e4b"/></svg></div>
    <p>Licensed and insured</p>
  </div>
  <div class="feature" style="left:829px">
    <div class="tile"><svg width="40" height="40" viewBox="0 0 40 40"><path d="M8 16l6-7h12l6 7-12 15z" stroke="#333" stroke-width="2" fill="none"/><path d="M8 16h24M16 9l4 22 4-22" stroke="#0d5e4b" stroke-width="1.5" fill="none"/></svg></div>
    <p>Quality and value assurance</p>
  </div>
  <div class="dots" style="left:570px;top:186px;gap:8px"><span class="small-dot"></span><span class="small-dot on"></span><span class="small-dot"></span></div>
</section>

<h2 class="section-title" style="top:3228px"><span>PAR</span>TNERS</h2>
<div class="arrow grey" style="left:106px;top:3332px"><svg width="12" height="12" viewBox="0 0 12 12"><path d="M8 2L4 6l4 4" stroke="#fff" stroke-width="2" fill="none"/></svg></div>
<div class="arrow green" style="left:1069px;top:3332px"><svg width="12" height="12" viewBox="0 0 12 12"><path d="M4 2l4 4-4 4" stroke="#fff" stroke-width="2" fill="none"/></svg></div>
<div class="partner" style="left:150px"><div class="mark"><i style="background:#6fc7a4"></i><b></b></div></div>
<div class="partner" style="left:380px"><div class="mark"><i style="background:#e6a23c"></i><b></b></div></div>
<div class="partner" style="left:610px"><div class="mark"><i style="background:#2c8fc9"></i><b></b></div></div>
<div class="partner" style="left:842px"><div class="mark"><i style="background:#d9383a"></i><b></b></div></div>
<div class="btn" style="left:484px;top:3420px;width:96px">Call Us</div>
<div class="btn teal" style="left:586px;top:3420px;width:128px">Get a Quote</div>

<section class="abs testimonial">
  <div class="rating">
    <svg width="118" height="18" viewBox="0 0 118 18"><g fill="#3fbf9e"><path id="st" d="M9 1l2.4 5.2 5.6.6-4.2 3.8 1.2 5.6L9 13.3 4 16.2l1.2-5.6L1 6.8l5.6-.6z"/><use href="#st" x="24"/><use href="#st" x="48"/><use href="#st" x="72"/></g><path d="M105 1l2.4 5.2 5.6.6-4.2 3.8 1.2 5.6-5-2.9-5 2.9 1.2-5.6-4.2-3.8 5.6-.6z" fill="none" stroke="#3fbf9e" stroke-width="1.3"/></svg>
    <span style="margin-left:8px">4.5</span>
  </div>
  <p class="quote">We just completed an auction that raised over $30,000 for a family battling cancer. Bidwell Auctions made it possible with very little cost. 100% we will use them again.</p>
  <div class="rule"></div>
  <svg class="abs" style="left:208px;top:250px" width="62" height="46" viewBox="0 0 62 46"><path d="M24 6C10 10 4 20 6 30c2 8 12 10 16 4s-2-14-10-10M54 6C40 10 34 20 36 30c2 8 12 10 16 4s-2-14-10-10" stroke="#3fbf9e" stroke-width="2" fill="none"/></svg>
  <div class="author"><span class="name">Peter Hollis</span><br>Ashford Family Fund</div>
  <div class="vdots"><span class="small-dot"></span><span class="small-dot"></span><span class="small-dot on"></span><span class="small-dot"></span></div>
  <div class="abs" style="left:862px;top:67px;width:236px;height:236px;border-radius:50%;border:6px solid #3fbf9e;background:radial-gradient(ellipse 80px 95px at 50% 42%,#d2ad93 0%,#8f6b55 50%,transparent 75%),linear-gradient(180deg,#f2f2f2 0%,#e6e6e6 62%,#3a3a3a 85%,#222 100%)" role="img" aria-label="Portrait photo of the client giving the testimonial"></div>
</section>

<h2 class="section-title" style="top:3978px"><span>GET</span> IN TOUCH</h2>
<div class="field" style="left:302px;top:4051px;width:290px"><svg width="12" height="12" viewBox="0 0 12 12"><circle cx="6" cy="4" r="2.5" stroke="#999" fill="none"/><path d="M1.5 11.5c0-3 2-4.5 4.5-4.5s4.5 1.5 4.5 4.5" stroke="#999" fill="none"/></svg>First Name</div>
<div class="field" style="left:608px;top:4051px;width:290px"><svg width="12" height="12" viewBox="0 0 12 12"><circle cx="6" cy="4" r="2.5" stroke="#999" fill="none"/><path d="M1.5 11.5c0-3 2-4.5 4.5-4.5s4.5 1.5 4.5 4.5" stroke="#999" fill="none"/></svg>Last Name</div>
<div class="field" style="left:302px;top:4102px;width:290px"><svg width="12" height="12" viewBox="0 0 12 12"><rect x="1" y="2.5" width="10" height="7" stroke="#999" fill="none"/><path d="M1 3l5 3.5L11 3" stroke="#999" fill="none"/></svg>Email</div>
<div class="field" style="left:608px;top:4102px;width:290px"><svg width="12" height="12" viewBox="0 0 12 12"><rect x="3" y="1" width="6" height="10" rx="1" stroke="#999" fill="none"/></svg>Phone</div>
<div class="field" style="left:302px;top:4156px;width:596px;height:94px;align-items:flex-start;padding-top:12px"><svg width="12" height="12" viewBox="0 0 12 12"><path d="M2 10l1-3 6-6 2 2-6 6z" stroke="#999" fill="none"/></svg>How can we help?</div>
<div class="btn" style="left:556px;top:4280px;width:88px">Submit</div>

<footer class="abs site-footer">
  <div class="footer-brand">Brookhollow Paint</div>
  <p class="abs" style="left:88px;top:128px;font-size:12px;color:#ddd">NJ Lic: #27KB08812300</p>
  <div class="btn" style="left:86px;top:168px;width:162px">Get an Estimate</div>

  <div class="col-title" style="left:408px;top:62px">Conatct Info</div>
  <div class="contact-line" style="top:98px"><svg width="13" height="13" viewBox="0 0 24 24"><path fill="#12a38a" d="M6.6 10.8a15 15 0 006.6 6.6l2.2-2.2c.3-.3.7-.4 1-.2 1.1.4 2.3.6 3.6.6.6 0 1 .4 1 1V20c0 .6-.4 1-1 1A17 17 0 013 4c0-.6.4-1 1-1h3.5c.6 0 1 .4 1 1 0 1.3.2 2.5.6 3.6.1.3 0 .7-.2 1z"/></svg>+1 555-014-2290</div>
  <div class="contact-line" style="top:140px"><svg width="14" height="13" viewBox="0 0 14 12"><rect x="1" y="1.5" width="12" height="9" fill="#12a38a"/><path d="M1 2l6 4.5L13 2" stroke="#232323" fill="none"/></svg>info@brookhollowpaint.com</div>
  <div class="contact-line" style="top:182px"><svg width="13" height="16" viewBox="0 0 12 16"><path d="M6 0a6 6 0 016 6c0 4.5-6 10-6 10S0 10.5 0 6a6 6 0 016-6z" fill="#12a38a"/><circle cx="6" cy="6" r="2.2" fill="#232323"/></svg><span>48 Larkspur Road Suite 3,<br>Brookhollow, AL, United States,<br>Alabama</span></div>

  <div class="col-title" style="left:690px;top:42px">Quick Link</div>
  <ul class="quick-links">
    <li class="current">Home</li><li>About Us</li><li>Services</li><li>Industries</li><li>Testimonials</li><li>Contact Us</li>
  </ul>

  <div class="abs" style="left:864px;top:74px;width:248px;height:163px;background:radial-gradient(ellipse 120px 90px at 30% 40%,#eef2e4 0%,#e2ead6 60%,transparent 80%),linear-gradient(120deg,#dfe8d3 0%,#e9ecdf 50%,#cfe0c4 62%,#a9cbe9 74%,#8fb9e3 100%)" role="img" aria-label="Map showing the office location in the southeastern United States"></div>
  <div class="abs" style="left:1144px;top:211px;width:34px;height:34px;border-radius:50%;border:1.5px solid #12a38a;display:flex;align-items:center;justify-content:center"><svg width="14" height="14" viewBox="0 0 14 14"><path d="M7 12V3M3 6l4-4 4 4M3 1h8" stroke="#12a38a" stroke-width="1.5" fill="none"/></svg></div>
</footer>
<div class="abs footer-bar">
  <p class="abs" style="left:88px;top:9px;font-family:'Crimson Pro',serif;font-size:12px;color:#ddd">© 2023 Brookhollow Paint Contractors. All Right Reserved</p>
  <div class="social"><i></i><i style="background:#12a38a"></i><i></i><i></i></div>
</div>

</body>
</html>
```